We are full service plumbing contractors that are capable of performing all of your plumbing need...

A clean, crisp website that conveys we can handle any plumbing from drain cleaning, repairs, to new construction. But emphasis on Leak detection, under-slab and underground water service leaks, repairs, and reroutes. Leak detection by acoustical, Thermal, or tracer gas , methods.Also emphasize advanced drain cleaning technologies and equipment. Don't just poke ahole in the drain blockage, Clean the pipe, with our High pressure hydrojetters, or Chain knocker drain cables that expand to the width of the pipe being cleaned.

Number of Pages Required

5+ page

Font styles to use
Sans Serif

Requirements
Should not have
• Canned photos

```html
<!DOCTYPE html>
<html lang="en">
<head>
<meta charset="utf-8">
<title>Tidewell Plumbing</title>
<link rel="stylesheet" href="https://fonts.googleapis.com/css2?family=Montserrat:ital,wght@0,400;0,500;0,600;0,700;0,800;1,800&family=Oswald:wght@500;600&display=swap">
<style>
:root{
  --navy:#1c4483;
  --gold:#e9b84a;
  --gold-light:#f5d27a;
  --red:#e0151b;
  --red-dark:#b30e12;
  --ink:#111;
  --grey-text:#555;
  --footer:#3a3a3a;
  --footer-text:#e6e6e6;
  --footer-head:#9a9a9a;
  --field:#1f4f9a;
  --line:#dcdcdc;
}
*{box-sizing:border-box;margin:0;padding:0}
html,body{width:734px;height:1200px;overflow:hidden;background:#fff}
body{position:relative;font-family:"Montserrat",Arial,sans-serif;color:var(--ink)}
.abs{position:absolute}

/* header */
.header{left:0;top:0;width:734px;height:95px;background:var(--navy)}
.brand{left:170px;top:22px;display:flex;align-items:center;gap:6px;color:var(--gold);font-weight:800;font-size:19px;line-height:1;letter-spacing:.5px}
.brand-dot{width:12px;height:12px;border-radius:50%;background:var(--red)}
.call{left:400px;top:20px;font-family:"Oswald",Arial,sans-serif;font-weight:600;font-size:21px;line-height:1;color:var(--gold);letter-spacing:.3px}
.nav{left:163px;top:68px;width:408px;height:27px;background:#fff;display:flex;align-items:center;font-size:5.6px;font-weight:500;letter-spacing:.3px;border-top:3px solid #b8b8b8}
.nav a{color:#222;text-decoration:none}
.nav .home{background:#e9e3da;height:27px;margin-top:-3px;border-top:4px solid var(--red);display:flex;align-items:center;justify-content:center;width:41px;flex:none}
.nav-links{flex:1;display:flex;justify-content:space-between;align-items:center;padding:0 16px 0 20px}
.nav .sep{color:#444}
.gold-rule{left:0;top:95px;width:734px;height:2px;background:var(--gold)}

/* hero */
.hero{left:0;top:97px;width:734px;height:268px;background:linear-gradient(135deg,#3f6b4a 0%,#5f8a5a 35%,#7d6a5c 60%,#5d6b7e 100%)}
.hero-tint{left:0;top:97px;width:734px;height:268px;background:rgba(28,68,131,.45)}
.hero-base{left:0;top:363px;width:734px;height:3px;background:var(--navy)}
.hero-title{left:170px;top:102px;font-weight:800;font-style:italic;font-size:23.5px;line-height:25px;color:var(--gold-light);letter-spacing:.8px}
.photo-circle{border-radius:50%;border:4px solid #8b8360}
.circle-big{left:252px;top:160px;width:184px;height:184px;background:radial-gradient(circle at 55% 45%,#6b5a43,#3e5a34 70%)}
.circle-small{left:163px;top:228px;width:86px;height:86px;background:linear-gradient(180deg,#5a8fd4 0%,#e8eef4 55%,#5f8d3e 100%)}
.form-title{left:452px;top:115px;font-family:"Oswald",Arial,sans-serif;font-weight:500;font-size:15px;line-height:1;color:#fff}
.form-note{left:454px;top:134px;width:110px;font-size:5.8px;line-height:7px;color:#fff}
.form-phone{left:454px;top:150px;font-family:"Oswald",Arial,sans-serif;font-weight:600;font-size:20px;line-height:1;color:var(--red)}
.field{left:454px;width:116px;background:var(--field);border:1px solid #4a78bd;color:#fff;font-size:5.5px;padding:4px 6px}
.submit{left:513px;top:284px;width:57px;height:18px;background:var(--red);color:#fff;font-size:8px;font-weight:600;display:flex;align-items:center;justify-content:center;border-bottom:2px solid var(--red-dark)}

/* services */
.service-img{top:385px;width:132px;height:70px}
.service-title{top:458px;font-size:11px;line-height:1.2;font-weight:500}
.service-text{top:472px;width:130px;font-size:5.4px;line-height:8px;color:var(--grey-text)}
.btn{height:18px;background:var(--red);color:#fff;font-size:5.8px;font-weight:600;display:flex;align-items:center;justify-content:center;border-bottom:2px solid var(--red-dark)}
.service-btn{top:525px;width:58px}

/* about */
.about-img{left:163px;top:588px;width:209px;height:157px;background:linear-gradient(180deg,#9fb6c8 0%,#6e8a5e 35%,#e9ecef 55%,#8d8d8a 100%)}
.about-title{left:383px;top:586px;font-size:16px;line-height:1.2;font-weight:600;letter-spacing:.5px}
.about-text{left:383px;top:612px;width:184px;font-size:5.4px;line-height:8.8px;color:var(--grey-text)}
.about-btn{left:383px;top:715px;width:58px}

/* testimonials */
.t-title{left:0;width:734px;top:772px;text-align:center;font-size:16px;line-height:1.2;font-weight:600;letter-spacing:.6px}
.t-sub{left:0;width:734px;top:793px;text-align:center;font-size:6.5px;font-weight:500;color:var(--grey-text)}
.t-card{top:820px;width:167px;height:66px;background:#fff;border:1px solid var(--line);border-top:3px solid var(--red);padding:7px 10px;font-size:5.4px;line-height:8.8px;color:#444}
.t-card::after{content:"";position:absolute;left:78px;bottom:-6px;width:9px;height:9px;background:#fff;border-right:1px solid var(--line);border-bottom:1px solid var(--line);transform:rotate(45deg)}
.arrow{top:846px;width:19px;height:19px;border-radius:50%;background:#e3e3e3}
.avatar{top:896px;width:35px;height:35px;border-radius:50%;border:2px solid #ddd;background:linear-gradient(180deg,#d9d9d9,#b7b7b7)}
.t-name{top:935px;width:120px;text-align:center;font-size:7.5px;font-weight:600}
.t-role{top:945px;width:120px;text-align:center;font-size:6px;color:#888}

/* cta */
.worker{left:164px;top:983px;width:68px;height:99px;background:linear-gradient(180deg,#b9b2a6 0%,#2e4a74 30%,#22385a 100%);border-radius:30px 30px 0 0}
.cta{left:0;top:1047px;width:734px;height:35px;background:var(--red)}
.cta-text{left:236px;top:1059px;font-family:"Oswald",Arial,sans-serif;font-weight:500;font-size:9.2px;line-height:1;color:#fff;white-space:nowrap}
.cta-btn{left:467px;top:1056px;width:99px;height:18px;background:#fff;color:var(--red);font-size:5.8px;font-weight:600;display:flex;align-items:center;justify-content:center;border:1px solid #ddd}

/* footer */
.footer{left:0;top:1082px;width:734px;height:96px;background:var(--footer)}
.f-col{top:1091px;color:var(--footer-text);font-size:5.4px;line-height:10.2px}
.f-col h4{font-size:8px;font-weight:500;color:var(--footer-head);margin-bottom:3px;letter-spacing:.3px}
.f-div{top:1096px;width:1px;height:70px;background:#555}
.copyright{left:0;top:1178px;width:734px;height:22px;text-align:center;font-size:6.2px;line-height:22px;color:#444}
</style>
</head>
<body>

<header class="abs header"></header>
<div class="abs brand"><span class="brand-dot"></span>Tidewell</div>
<div class="abs call">CALL 610.555.0148</div>
<nav class="abs nav">
  <a class="home">HOME</a>
  <div class="nav-links">
    <a>SERVICES</a><span class="sep">|</span>
    <a>INDUSTRIES</a><span class="sep">|</span>
    <a>ABOUT US</a><span class="sep">|</span>
    <a>LOCATIONS</a><span class="sep">|</span>
    <a>BLOG</a><span class="sep">|</span>
    <a>CONTACT US</a>
  </div>
</nav>
<div class="abs gold-rule"></div>

<section class="abs hero" role="img" aria-label="Garden with brick edging and plants behind the hero"></section>
<div class="abs hero-tint"></div>
<div class="abs hero-base"></div>
<h1 class="abs hero-title">REPLACE THE PIPE<br>WITHOUT MESS</h1>
<div class="abs photo-circle circle-big" role="img" aria-label="Leak detection equipment beside an excavated pipe in a lawn"></div>
<div class="abs photo-circle circle-small" role="img" aria-label="Service van parked on a driveway"></div>

<h2 class="abs form-title">CONTACT US ONLINE</h2>
<p class="abs form-note">To get a free estimate, please fill out the form below or call us now at</p>
<div class="abs form-phone">610-555-0148</div>
<div class="abs field" style="top:174px;height:17px">* Name</div>
<div class="abs field" style="top:195px;height:16px">* Email</div>
<div class="abs field" style="top:213px;height:16px">* Phone</div>
<div class="abs field" style="top:231px;height:49px">* Message</div>
<div class="abs submit">SUBMIT</div>

<div class="abs service-img" style="left:163px;background:linear-gradient(135deg,#a8a39a,#6d6a63 60%,#8b7a5e)" role="img" aria-label="Exposed residential pipe among rocks"></div>
<div class="abs service-img" style="left:301px;background:linear-gradient(135deg,#cfc8c0,#7c7a78 60%,#b9aa94)" role="img" aria-label="Commercial drain cleaning machine"></div>
<div class="abs service-img" style="left:438px;background:linear-gradient(135deg,#8a6b55,#3f3a36 60%,#6f7d8a)" role="img" aria-label="Industrial pipework and cabling"></div>

<h3 class="abs service-title" style="left:166px">Residential Services</h3>
<h3 class="abs service-title" style="left:305px">Commercial Services</h3>
<h3 class="abs service-title" style="left:441px">Industrial Services</h3>
<p class="abs service-text" style="left:166px">Leak detection by acoustic, thermal and tracer gas methods. We locate under-slab and underground water service leaks, then repair or reroute the line with minimal mess.</p>
<p class="abs service-text" style="left:305px">Advanced drain cleaning: high pressure hydrojetters and chain knocker cables expand to the full pipe width, so we clean the pipe instead of poking a hole.</p>
<p class="abs service-text" style="left:441px">Repairs, reroutes and new construction piping for plants and facilities, handled by one crew.</p>
<div class="abs btn service-btn" style="left:200px">READ MORE</div>
<div class="abs btn service-btn" style="left:338px">READ MORE</div>
<div class="abs btn service-btn" style="left:475px">READ MORE</div>

<div class="abs about-img" role="img" aria-label="Company service vans parked at the shop"></div>
<h2 class="abs about-title">ABOUT US</h2>
<p class="abs about-text">We are full service plumbing contractors, ready for every job from drain cleaning and repairs to new construction. Our specialty is leak detection: acoustic listening, thermal imaging and tracer gas let us pinpoint under-slab and underground water service leaks without tearing up your property, then repair or reroute the line.<br>For blocked drains we bring hydrojetters and chain knocker cables that scour the pipe wall clean.</p>
<div class="abs btn about-btn">CONTACT US</div>

<h2 class="abs t-title">TESTIMONIAL</h2>
<p class="abs t-sub">What our valuable client says</p>
<div class="abs arrow" style="left:165px">
  <svg width="19" height="19" viewBox="0 0 19 19"><path d="M11 6 L7.5 9.5 L11 13" fill="none" stroke="#666" stroke-width="1"/></svg>
</div>
<div class="abs arrow" style="left:550px">
  <svg width="19" height="19" viewBox="0 0 19 19"><path d="M8 6 L11.5 9.5 L8 13" fill="none" stroke="#666" stroke-width="1"/></svg>
</div>
<div class="abs t-card" style="left:190px">Lorem ipsum dolor sit amet, consectetur adipisicing elit, sed do eiusmod tempor incididunt ut labore et dolore magna aliqua. Ut enim ad minim veniam, quis nostrud exercit Lorem ipsum dolor sit amet, consectetur adipisicing elit, sed do eiusmod tempor</div>
<div class="abs t-card" style="left:376px">Lorem ipsum dolor sit amet, consectetur adipisicing elit, sed do eiusmod tempor incididunt ut labore et dolore magna aliqua. Ut enim ad minim veniam, quis nostrud exercit Lorem ipsum dolor sit amet, consectetur adipisicing elit, sed do eiusmod tempor</div>
<div class="abs avatar" style="left:259px" role="img" aria-label="Client portrait"></div>
<div class="abs avatar" style="left:445px" role="img" aria-label="Client portrait"></div>
<div class="abs t-name" style="left:216px">Daniel Brooks</div>
<div class="abs t-role" style="left:216px">Company Owner</div>
<div class="abs t-name" style="left:402px">Maria Lenton</div>
<div class="abs t-role" style="left:402px">House Owner</div>

<div class="abs cta"></div>
<div class="abs worker" role="img" aria-label="Plumber in uniform holding a clipboard, giving a thumbs up"></div>
<div class="abs cta-text">Schedule a Service with TIDEWELL Today! Call: 610-555-0148</div>
<div class="abs cta-btn">REQUEST APPOINTMENT</div>

<footer class="abs footer"></footer>
<div class="abs f-col" style="left:163px">
  <h4>NAVIGATION</h4>
  HOME<br>SERVICES<br>ABOUT US<br>LOCATIONS<br>BLOG<br>CONTACT US
</div>
<div class="abs f-div" style="left:259px"></div>
<div class="abs f-col" style="left:302px">
  <h4>INDUSTRIES SERVED</h4>
  RESIDENTIAL<br>COMMERCIAL<br>INDUSTRIAL<br>MUNICIPAL<br>SPECIALTY PROJECTS
</div>
<div class="abs f-div" style="left:430px"></div>
<div class="abs f-col" style="left:474px">
  <h4>CONTACT US</h4>
  ADDRESS:<br>418 MILLBROOK ROAD<br>CEDAR FALLS, PA 19400 USA<br><br>EMAIL: info@tidewellplumbing.com<br>PHONE: 610-555-0148
</div>
<div class="abs copyright">Copyright © 2019 TidewellPlumbing.com.</div>

</body>
</html>
```